business card and flyer/pricelist

Business Name: Willow Strand Salon
new boutique salon run from home, using Australian owned natural products and colours, we need a flyer design to do a letter box drop to advertise the business as well as incorporating a price list on the front (single sided with writing on front and only colour on back)

The salon has a natural feel with light coloured timber chairs, bamboo timber bench top and shelving.

we are after a natural toned colour for the flyer, with possibly a brown/darkish colour writing

we are after a flyer that will also be able to use the design heading (business name) for business cards as well

feel free to look on my pintrest account to get a feel for my style under Corinne Belvane.

I love simple clean and Natural looks.

Industry/Entity Type

Boutique

Font styles to use
Script
Other font styles liked:
• SCRIPT HANDWRITTEN FONTS

Colors
cadf82
e9f1ce
5c5c5c
d3d3d3
add136
fee18a

Requirements
Must have
• NATURAL COLOURINGS, eg soft greens, browns,
white or off white background.
Should not have
• photos,

```html
<!DOCTYPE html>
<html lang="en">
<head>
<meta charset="utf-8">
<title>Willow Strand Salon – Price List</title>
<link rel="stylesheet" href="https://fonts.googleapis.com/css2?family=Lobster&family=Raleway:wght@300;400&display=swap">
<style>
  :root {
    --paper: #f4e6cc;
    --band: #dcbb8d;
    --wave-line: #c9a57a;
    --title-green: #86a33a;
    --intro-lead: #86995a;
    --intro-body: #8f9a76;
    --ink: #5c5c5c;
    --row-top: #dcd7c1;
    --row-bottom: #cdc7ad;
    --row-edge: #a8a48e;
    --head-top: #e6e9d8;
    --head-bottom: #b8bda6;
    --flower-pink: #ec8fc0;
    --flower-green: #5a9a3e;
    --leaf-yellow: #dfe43e;
  }
  * { box-sizing: border-box; margin: 0; padding: 0; }
  html, body {
    width: 1200px;
    height: 2609px;
    overflow: hidden;
    background: var(--paper);
  }
  .flyer {
    position: relative;
    width: 1200px;
    height: 2609px;
    background: var(--paper);
    overflow: hidden;
    font-family: "Raleway", "Helvetica Neue", Arial, sans-serif;
  }
  .flyer__waves {
    position: absolute;
    inset: 0;
    width: 1200px;
    height: 2609px;
  }
  .flyer__title {
    position: absolute;
    top: 205px;
    left: 0;
    width: 1200px;
    text-align: center;
    font-family: "Lobster", "Brush Script MT", cursive;
    font-weight: 400;
    font-size: 124px;
    line-height: 1;
    color: var(--title-green);
  }
  .intro {
    position: absolute;
    top: 530px;
    left: 64px;
    width: 780px;
    font-weight: 300;
    font-size: 64px;
    line-height: 66px;
    color: var(--intro-body);
  }
  .intro__name {
    display: block;
    font-weight: 400;
    font-size: 68px;
    color: var(--intro-lead);
  }
  .flower {
    position: absolute;
    left: 840px;
    top: 430px;
    width: 360px;
    height: 2090px;
    border-radius: 180px 180px 40px 200px;
    background: linear-gradient(180deg,
      var(--flower-pink) 0%,
      #e25a9e 18%,
      #a9c94a 30%,
      var(--leaf-yellow) 40%,
      #7fb545 60%,
      var(--flower-green) 100%);
    opacity: 0.9;
  }
  .price-list {
    position: absolute;
    left: 33px;
    top: 1180px;
    width: 804px;
    list-style: none;
  }
  .price-list__row {
    display: flex;
    justify-content: space-between;
    align-items: center;
    height: 110px;
    margin-bottom: 6px;
    padding: 0 18px 0 24px;
    background: linear-gradient(180deg, var(--row-top), var(--row-bottom));
    border: 2px solid var(--row-edge);
    border-radius: 8px;
    box-shadow: 0 3px 4px rgba(90, 80, 60, 0.35);
    color: var(--ink);
    font-weight: 300;
  }
  .price-list__row--head {
    height: 150px;
    background: linear-gradient(180deg, var(--head-top), var(--head-bottom));
  }
  .price-list__row--head .price-list__item,
  .price-list__row--head .price-list__price {
    font-size: 66px;
  }
  .price-list__item { font-size: 56px; }
  .price-list__price { font-size: 48px; }
</style>
</head>
<body>
<main class="flyer">
  <svg class="flyer__waves" viewBox="0 0 1200 2609" aria-hidden="true">
    <path fill="var(--band)" d="M0,0 H1200 V120 C1050,180 900,70 700,110 C520,150 380,190 200,150 C110,130 50,115 0,130 Z"/>
    <path fill="none" stroke="var(--wave-line)" stroke-width="38" d="M0,405 C250,385 450,440 720,425 C950,412 1080,395 1200,410"/>
    <path fill="none" stroke="var(--wave-line)" stroke-width="38" d="M0,950 C220,925 420,1000 680,975 C920,952 1080,985 1200,1000"/>
    <path fill="var(--band)" d="M0,2470 C200,2430 380,2490 600,2460 C820,2430 1000,2420 1200,2470 V2609 H0 Z"/>
  </svg>

  <h1 class="flyer__title">Willow Strand Salon</h1>

  <p class="intro">
    <span class="intro__name">Willow Strand Salon</span>
    is a new boutique salon run from home, using Australian owned natural products and colours.
  </p>

  <div class="flower" role="img" aria-label="Illustration of a pink tulip with green leaves and stem"></div>

  <ul class="price-list">
    <li class="price-list__row price-list__row--head"><span class="price-list__item">Product</span><span class="price-list__price">Price</span></li>
    <li class="price-list__row"><span class="price-list__item">Cut &amp; Blowdry</span><span class="price-list__price">from $23</span></li>
    <li class="price-list__row"><span class="price-list__item">Wet Cut</span><span class="price-list__price">from $15</span></li>
    <li class="price-list__row"><span class="price-list__item">Dry Cut</span><span class="price-list__price">from $10</span></li>
    <li class="price-list__row"><span class="price-list__item">Blow Dry</span><span class="price-list__price">from $13</span></li>
    <li class="price-list__row"><span class="price-list__item">Blow Dry(long hair)</span><span class="price-list__price">from $16</span></li>
    <li class="price-list__row"><span class="price-list__item">Semi Colour</span><span class="price-list__price">from $40</span></li>
    <li class="price-list__row"><span class="price-list__item">Tint Roots</span><span class="price-list__price">from $45</span></li>
    <li class="price-list__row"><span class="price-list__item">Full Head Foils</span><span class="price-list__price">from $60</span></li>
  </ul>
</main>
</body>
</html>
```